Recruitment Web Site Design

I need a Recruitment website explaining who we are and what services we deliver.
This is a new company and the image we portray is extremely important. Must be very professional.
Our target marget are bluechip companies and professionals including executives.

The final design should communicate connecting professionals matching company and individual needs.

Target Market(s)

Corporate, Blue Chip Companies, Professionals/Executives

Industry/Entity Type

It Company

Requirements
Must have
• Must be professional and Sophisticated.
Must have a few tabs.

Must be unique to the norm of websites as I am looking for something different.
Nice to have
• Good graphics with people connecting. Multi - racial pics will be good as we are in South Africa and diversity is a must.
Also a front page (be unique).

I am putting this out there for you to use your imagination and come up with something brilliant.

A few websites you can base ideas from

www.maplevertex.com
www.thestaffnook.co.za
www.kvt.co.za
www.rul.co.za

```html
<!DOCTYPE html>
<html lang="en">
<head>
<meta charset="utf-8">
<title>Corvane Recruitment</title>
<link rel="stylesheet" href="https://fonts.googleapis.com/css2?family=Arimo:wght@400;700&family=Ubuntu:wght@500;700&family=Merriweather:wght@900&family=PT+Sans+Narrow:wght@700&display=swap">
<style>
:root{
  --red:#d40000;
  --red-dark:#a80000;
  --ink:#111;
  --text:#333;
  --grey-1:#f2f2f2;
  --grey-2:#d9d9d9;
  --grey-3:#9a9a9a;
  --grey-4:#6d6d6d;
  --white:#fff;
}
*{box-sizing:border-box;margin:0;padding:0}
html,body{width:1156px;height:1200px;overflow:hidden}
body{position:relative;font-family:"Arimo",Arial,sans-serif;color:var(--text);
  background:linear-gradient(#e8e8e8 0,#cfcfcf 180px,#efefef 190px,#f3f3f3 100%)}
.abs{position:absolute}
.page{position:absolute;left:126px;top:180px;width:906px;height:920px;background:var(--white);box-shadow:0 0 12px rgba(0,0,0,.25)}
/* header */
.brand{left:128px;top:50px;display:flex;align-items:center;gap:14px}
.brand-mark{width:40px;height:40px;background:var(--red)}
.brand-name{font-family:"Arimo",Arial,sans-serif;font-size:40px;letter-spacing:8px;color:#444;line-height:1}
.brand-sub{font-size:14px;letter-spacing:7px;color:#444;margin-top:6px}
.phone{right:138px;top:30px;display:flex;align-items:center;gap:10px;font-weight:700;font-size:15px;color:var(--ink)}
.search{left:780px;top:70px;width:251px;height:29px;border:1px solid var(--red);border-radius:8px;background:var(--white);display:flex;overflow:hidden}
.search span{flex:1;padding:7px 11px;font-size:13px;color:#888}
.search i{width:34px;background:linear-gradient(#999,#555);display:flex;align-items:center;justify-content:center}
/* nav */
.nav{left:126px;top:155px;width:905px;height:70px}
.nav ul{position:absolute;left:30px;top:28px;display:flex;list-style:none}
.nav li{color:var(--white);font-size:13px;padding:0 26px;border-left:1px solid #bbb;line-height:18px}
.nav li:first-child{border-left:0;padding-left:26px}
/* hero */
.hero{left:126px;top:225px;width:905px;height:302px;background:linear-gradient(#dcdcdc,#f4f4f4 60%,#d6d6d6)}
.hero-art{left:400px;top:0;width:505px;height:302px;background:linear-gradient(90deg,rgba(220,220,220,0),#9b9b9b 20%,#c4c4c4 60%,#8e8e8e)}
.hero-skyline{left:0;top:16px;width:905px;height:30px;background:linear-gradient(#bdbdbd,#8d8d8d);opacity:.7}
.hero-title{left:28px;top:70px;font-family:"Merriweather",Georgia,serif;font-weight:900;font-size:43px;color:var(--red);letter-spacing:-1px}
.hero-sub{left:32px;top:128px;font-family:"PT Sans Narrow",Arial,sans-serif;font-size:31px;line-height:34px;color:var(--ink)}
.btn{background:linear-gradient(#ff2a2a,#c80000);color:var(--white);font-family:"Ubuntu",sans-serif;font-weight:700;border-radius:8px;box-shadow:0 2px 3px rgba(0,0,0,.45);display:flex;align-items:center;justify-content:center}
.hero-btn{left:30px;top:205px;width:239px;height:40px;font-size:22px;gap:10px;font-weight:500}
.dots{left:559px;top:529px;display:flex;gap:5px}
.dots i{width:11px;height:11px;border-radius:50%;background:#333}
.dots i:first-child{background:var(--red)}
/* panels */
.panel-h{font-family:"Ubuntu",sans-serif;font-weight:500;font-size:22px;color:var(--ink)}
.panel-p{font-size:11px;line-height:13px;color:var(--white)}
.panel-art{border-radius:4px}
.field{width:201px;height:30px;background:var(--white);border:1px solid var(--red);border-radius:7px}
.small-btn{height:27px;font-size:13px}
.login-links{left:795px;top:724px;font-family:"Ubuntu",sans-serif;font-weight:500;font-size:13px;color:var(--white)}
.login-links u{margin:0 5px}
/* content */
.welcome{left:150px;top:832px;width:560px}
.section-h{font-family:"Ubuntu",sans-serif;font-weight:500;font-size:22px;color:var(--ink);margin-bottom:8px}
.welcome p{font-size:12.7px;line-height:16.2px;color:var(--text);padding-left:3px;margin-bottom:16px}
.divider{left:731px;top:845px;width:1px;height:210px;background:#ccc}
.services{left:747px;top:832px}
.services ul{list-style:none}
.services li{font-size:12.7px;line-height:21.6px;color:var(--text);padding-left:22px;position:relative}
.services li::before{content:"";position:absolute;left:3px;top:7px;width:7px;height:7px;background:var(--red);transform:rotate(45deg)}
/* footer */
.footer{left:0;top:1092px;width:1156px;height:108px;background:linear-gradient(#f2f2f2,#cfcfcf)}
.foot-links{left:144px;top:1128px;font-size:13px;color:var(--ink)}
.foot-links span{margin:0 5px}
.copy{left:144px;top:1153px;font-size:11px;color:var(--ink)}
.foot-rule{left:731px;top:1096px;width:1px;height:104px;background:#8a8a8a}
.social{left:853px;top:1120px;display:flex;gap:10px}
.social i{width:22px;height:22px;border-radius:4px;background:#6e7f96}
.foot-brand{left:800px;top:1146px;display:flex;align-items:center;gap:10px}
.foot-brand .brand-mark{width:28px;height:28px}
.foot-brand .brand-name{font-size:24px;letter-spacing:4px}
</style>
</head>
<body>
<div class="page"></div>

<header>
  <div class="abs brand">
    <div class="brand-mark"></div>
    <div><div class="brand-name">CORVANE</div><div class="brand-sub">RECRUITMENT</div></div>
  </div>
  <div class="abs phone">
    <svg width="32" height="22" viewBox="0 0 32 22" aria-hidden="true"><path d="M2 8c4-6 24-6 28 0l-3 3-5-2V6H10v3l-5 2z" fill="#111"/><rect x="7" y="11" width="18" height="10" rx="2" fill="#111"/><circle cx="16" cy="16" r="3" fill="#fff"/></svg>
    01 555 0142 770
  </div>
  <div class="abs search"><span>Search:</span><i><svg width="18" height="18" viewBox="0 0 18 18" aria-hidden="true"><circle cx="10" cy="7" r="5" fill="none" stroke="#fff" stroke-width="2"/><path d="M6 11l-4 5" stroke="#fff" stroke-width="3"/></svg></i></div>
</header>

<nav class="abs nav">
  <svg class="abs" width="905" height="70" viewBox="0 0 905 70" aria-hidden="true">
    <defs><linearGradient id="navg" x1="0" y1="0" x2="0" y2="1"><stop offset="0" stop-color="#9a9a9a"/><stop offset="1" stop-color="#5e5e5e"/></linearGradient></defs>
    <polygon points="18,12 895,12 878,60 0,60" fill="url(#navg)"/>
    <polygon points="0,60 878,60 874,67 4,67" fill="var(--red)"/>
    <polygon points="895,12 905,0 885,67 878,60" fill="var(--red)"/>
  </svg>
  <ul><li>HOME</li><li>SEARCH</li><li>JOB LIST</li><li>EMPLOYER LIST</li><li>NEW JOBS</li><li>REFERENCES</li><li>CONTACT US</li></ul>
</nav>

<section class="abs hero">
  <div class="abs hero-skyline" role="img" aria-label="City skyline sketch"></div>
  <div class="abs hero-art" role="img" aria-label="Two smiling professionals leaning forward beside a thoughtful businessman on giant puzzle pieces"></div>
  <h1 class="abs hero-title">QUICKER ACCESS</h1>
  <p class="abs hero-sub">to the right talent<br>for you</p>
  <div class="abs btn hero-btn">Get Started Now
    <svg width="14" height="18" viewBox="0 0 14 18" aria-hidden="true"><path d="M3 2l8 7-8 7" fill="none" stroke="#fff" stroke-width="4"/></svg></div>
</section>
<div class="abs dots"><i></i><i></i><i></i></div>

<svg class="abs" style="left:134px;top:550px" width="900" height="230" viewBox="0 0 900 230" aria-hidden="true">
  <defs><linearGradient id="pg" x1="0" y1="0" x2="0" y2="1"><stop offset="0" stop-color="#e9e9e9"/><stop offset="1" stop-color="#6e6e6e"/></linearGradient></defs>
  <polygon points="25,2 580,2 556,220 0,220" fill="url(#pg)"/>
  <polygon points="580,0 586,6 562,226 556,220" fill="var(--red)"/>
  <polygon points="0,220 556,220 562,226 6,226" fill="var(--red)"/>
  <line x1="288" y1="8" x2="280" y2="215" stroke="#fff" stroke-opacity=".6"/>
  <polygon points="632,2 884,2 860,220 607,220" fill="url(#pg)"/>
  <polygon points="884,0 890,6 866,226 860,220" fill="var(--red)"/>
  <polygon points="607,220 860,220 866,226 613,226" fill="var(--red)"/>
</svg>

<section aria-label="Job seeker">
  <h2 class="abs panel-h" style="left:183px;top:562px">Job Seeker</h2>
  <p class="abs panel-p" style="left:183px;top:604px;width:105px">Lorem ipsum dolor sit amet, consectetur adipiscing elit. Nunc lorem diam, adipi-scing non cursus lobortis, luctus scelerisque turpis.</p>
  <div class="abs panel-art" role="img" aria-label="Framed certificate with thumbs-up icons" style="left:292px;top:600px;width:115px;height:105px;background:linear-gradient(135deg,#c9c9c9,#8e8e8e)"></div>
  <div class="abs btn small-btn" style="left:188px;top:717px;width:139px">Sign up for Free</div>
</section>
<div class="abs brand-mark" style="left:400px;top:745px;width:34px;height:34px"></div>

<section aria-label="Employer">
  <h2 class="abs panel-h" style="left:447px;top:560px">Employer</h2>
  <p class="abs panel-p" style="left:446px;top:604px;width:118px">Lorem ipsum dolor sit amet, consectetur adipi-scing elit. Nunc lorem diam, adipiscing non cursus lobortis, luctus scelerisque turpis. Nullam non mauris elit,</p>
  <div class="abs panel-art" role="img" aria-label="Magnifying glass over a target" style="left:585px;top:630px;width:106px;height:80px;background:linear-gradient(135deg,#b9c6d2,#7a7a7a)"></div>
  <div class="abs btn small-btn" style="left:511px;top:717px;width:94px">Sign Up</div>
</section>

<section aria-label="Login">
  <h2 class="abs panel-h" style="left:787px;top:560px">Login here</h2>
  <div class="abs brand-mark" style="left:960px;top:548px;width:26px;height:26px"></div>
  <div class="abs field" style="left:786px;top:602px"></div>
  <div class="abs field" style="left:786px;top:642px"></div>
  <div class="abs btn small-btn" style="left:785px;top:682px;width:94px">Sign In</div>
  <div class="abs login-links"><u>Forgot Password</u>|<u>New User</u></div>
</section>

<section class="abs welcome">
  <h2 class="section-h">Welcome to Corvane Recruitment</h2>
  <p>Lorem ipsum dolor sit amet, consectetur adipiscing elit. Nunc lorem diam, adipiscing non cursus lobortis, luctus scelerisque turpis. Nullam non mauris elit, eget imperdiet ligula. Donec porta quam cursus sapien lobortis sed aliquet augue auctor. Fusce laoreet, magna ultricies consectetur ornare, nisi augue eleifend arcu, a ornare sapien dui ut dui. Morbi cursus dui luctus magna fauci-bus euismod. Vestibulum ante ipsum primis in faucibus orci luctus et ultrices posuere cubilia Curae; Fusce in nisi magna, at mattis metus. Proin blandit mi quam, aliquam ullamcorper orci. Aliquam quis arcu nulla. Proin magna sem, facilisis vel hendrerit vel, viverra ut elit. Morbi et erat aliquam enim faucibus semper. Integer sollicitudin diam eget sem rutrum mattis.</p>
  <p>Mauris condimentum lacus leo, nec pulvinar ligula. Morbi sit amet tincidunt augue. Aenean quis eleifend nisi. Etiam tristique mauris mi. Proin tortor mi, sollicitudin non malesuada non, tincidunt eget nunc. Sed consequat porta tellus, eu sollicitudin leo posuere ac. Donec vel quam dui, id blan-</p>
</section>
<div class="abs divider"></div>
<section class="abs services">
  <h2 class="section-h">Our Services</h2>
  <ul>
    <li>Lorem ipsum dolor sit amet</li>
    <li>Consectetur adipiscing elit</li>
    <li>Nunc lorem diam adipiscing non cursus</li>
    <li>Lobortis luctus scelerisque turpis</li>
    <li>Nullam non mauris elit, eget imperdiet</li>
    <li>Ligula Donec porta quam cursus sapien</li>
    <li>Sed aliquet augue auctor Fusce laoreet</li>
    <li>Magna ultricies consectetur ornare nisi</li>
    <li>Augue eleifend arcu a ornare sapien dui</li>
  </ul>
</section>

<footer>
  <div class="abs footer"></div>
  <div class="abs foot-links">Home<span>|</span>Search<span>|</span>Job List<span>|</span>Employer List<span>|</span>New jobs<span>|</span>References<span>|</span>Contact Us</div>
  <div class="abs copy">Copyright © 2012 Brenlow.com All rights reserved!</div>
  <div class="abs foot-rule"></div>
  <div class="abs social"><i></i><i></i><i></i><i></i></div>
  <div class="abs foot-brand"><div class="brand-mark"></div><div class="brand-name">CORVANE</div></div>
</footer>
</body>
</html>
```